Twin Harbor Keystone Method

We are a wealth advisory firm. We need a design that shows our business is built on seven pillars. These seven pillars support all 85 things. These seven pillars form the foundation of our process. As their lives unfold and their needs evolve, they can’t outgrow our process; they’ll grow into it as critical life events occur and their lives progress.

We have an example of pillars, a figure of 8, and trees—we would like it to be modern, clean, and nature-inspired. If you use pillars, they cannot look 80s or like a law office. I am also attaching a picture of our logo and the landing page of our website for reference to our feel and style.
We want to use the language on the sheet with figure 8 in the final design.

Target Market(s)

families and small business owners with 1 million + of investable assets

Industry/Entity Type

Finance

Font styles to use
Sans Serif

Colors
0054AA
0677BA
7BADD7
CADEEF
E8F1F8
FFC000
F8CF3A
FAE287
FDF2CF
FEFAEE
EE7325
F08F49
F5BC92
FAE3D3
FDF4ED

```html
<!DOCTYPE html>
<html lang="en">
<head>
<meta charset="utf-8">
<title>Twin Harbor Keystone Method</title>
<link rel="stylesheet" href="https://fonts.googleapis.com/css2?family=Cinzel:wght@400;500&family=Montserrat:wght@500;600&display=swap">
<style>
  :root {
    --canvas: #ffffff;
    --ink-green: #163d2a;
    --roof: #1d5539;
    --band-green: #133a27;
    --band-orange: #e0620f;
    --accent-orange: #e0620f;
    --ledge: #c3d6cc;
    --plinth: #c8dbd2;
    --foliage: #9fbfa9;
    --foliage-deep: #3f5a4c;
    --col-1: #a2e1bf;
    --col-1-cap: #97dbb6;
    --col-2: #70d39b;
    --col-2-cap: #66cc92;
    --col-3: #5dcb8e;
    --col-3-cap: #55c486;
    --col-4: #2f9459;
    --col-4-cap: #2b8a52;
    --col-5: #256e42;
    --col-5-cap: #21663d;
    --col-6: #1b4d31;
    --col-6-cap: #18462d;
    --col-7: #143a27;
    --col-7-cap: #123524;
    --label-dark: #1a3626;
    --label-light: #ffffff;
  }
  html, body {
    margin: 0;
    padding: 0;
    width: 1200px;
    height: 1200px;
    overflow: hidden;
    background: var(--canvas);
  }
  .canvas { display: block; width: 1200px; height: 1200px; }
  .brand-name {
    font-family: "Montserrat", sans-serif;
    font-weight: 600;
    font-size: 13px;
    letter-spacing: 0.5px;
    fill: var(--ink-green);
  }
  .title {
    font-family: "Cinzel", serif;
    font-weight: 400;
    font-size: 40px;
    fill: var(--ink-green);
  }
  .tagline {
    font-family: "Montserrat", sans-serif;
    font-weight: 500;
    font-size: 13.5px;
    letter-spacing: 0.6px;
    fill: #ffffff;
  }
  .step-number {
    font-family: "Cinzel", serif;
    font-size: 30px;
    fill: #ffffff;
  }
  .pillar-label {
    font-family: "Montserrat", sans-serif;
    font-weight: 600;
    font-size: 9.5px;
    letter-spacing: 0.4px;
  }
  .pillar-label--dark { fill: var(--label-dark); }
  .pillar-label--light { fill: var(--label-light); }
  .base-label {
    font-family: "Cinzel", serif;
    font-size: 29px;
    fill: var(--ink-green);
  }
  .foliage { fill: var(--foliage); opacity: 0.75; }
  .foliage--deep { fill: var(--foliage-deep); opacity: 0.6; }
</style>
</head>
<body>
<svg class="canvas" viewBox="0 0 960 960" xmlns="http://www.w3.org/2000/svg">
  <!-- header -->
  <g class="brand">
    <circle cx="127" cy="243" r="11" fill="none" stroke="var(--ink-green)" stroke-width="2.5"/>
    <text class="brand-name" x="145" y="248">TWIN HARBOR</text>
  </g>
  <text class="title" x="255" y="260" textLength="483" lengthAdjust="spacingAndGlyphs">KEYSTONE METHOD</text>
  <rect x="257" y="267" width="241" height="29" fill="var(--band-green)"/>
  <rect x="498" y="267" width="242" height="29" fill="var(--band-orange)"/>
  <text class="tagline" x="377.5" y="286" text-anchor="middle">OUR PROCESS EVOLVES</text>
  <text class="tagline" x="619" y="286" text-anchor="middle">AS YOUR LIFE UNFOLDS</text>

  <!-- roof -->
  <polygon class="roof" points="490,323 843,432 155,432" fill="var(--roof)"/>
  <circle cx="490" cy="383" r="34" fill="none" stroke="var(--accent-orange)" stroke-width="2"/>
  <text class="step-number" x="490" y="394" text-anchor="middle">1</text>
  <rect class="ledge" x="153" y="434" width="690" height="10" fill="var(--ledge)"/>

  <!-- side foliage behind pillars -->
  <g role="img" aria-label="Leafy branch illustration on the left side">
    <ellipse class="foliage" cx="150" cy="650" rx="34" ry="58"/>
  </g>
  <g role="img" aria-label="Leafy branch illustration on the right side">
    <ellipse class="foliage" cx="845" cy="650" rx="36" ry="60"/>
  </g>

  <!-- pillars -->
  <g class="pillars">
    <polygon points="177,448 263,448 257,478 183,478" fill="var(--col-1-cap)"/>
    <rect x="185" y="478" width="72" height="214" fill="var(--col-1)"/>
    <text class="pillar-label pillar-label--dark" transform="translate(224,657) rotate(-90)">WEALTH MANAGEMENT</text>

    <polygon points="268,448 354,448 348,478 274,478" fill="var(--col-2-cap)"/>
    <rect x="274" y="478" width="72" height="214" fill="var(--col-2)"/>
    <text class="pillar-label pillar-label--dark" transform="translate(315,644) rotate(-90)">RISK MANAGEMENT</text>

    <polygon points="362,448 448,448 442,478 368,478" fill="var(--col-3-cap)"/>
    <rect x="368" y="478" width="73" height="214" fill="var(--col-3)"/>
    <text class="pillar-label pillar-label--dark" transform="translate(408,626) rotate(-90)">PHILANTHROPHY</text>

    <polygon points="455,448 542,448 536,478 461,478" fill="var(--col-4-cap)"/>
    <rect x="462" y="478" width="73" height="214" fill="var(--col-4)"/>
    <text class="pillar-label pillar-label--light" transform="translate(502,583) rotate(-90)">PERSONAL CFO</text>

    <polygon points="549,448 635,448 629,478 555,478" fill="var(--col-5-cap)"/>
    <rect x="556" y="478" width="72" height="214" fill="var(--col-5)"/>
    <text class="pillar-label pillar-label--light" transform="translate(596,651) rotate(-90)">CASH MANAGEMENT</text>

    <polygon points="643,448 729,448 723,478 649,478" fill="var(--col-6-cap)"/>
    <rect x="650" y="478" width="72" height="214" fill="var(--col-6)"/>
    <text class="pillar-label pillar-label--light" transform="translate(689,668) rotate(-90)">TAX &amp; ESTATE PLANNING</text>

    <polygon points="737,448 823,448 817,478 743,478" fill="var(--col-7-cap)"/>
    <rect x="744" y="478" width="71" height="214" fill="var(--col-7)"/>
    <text class="pillar-label pillar-label--light" transform="translate(783,680) rotate(-90)">PROFESSIONAL PARTNERSHIP</text>
  </g>

  <!-- foliage between pillars -->
  <g role="img" aria-label="Small leafy sprigs growing between the pillars">
    <ellipse class="foliage" cx="258" cy="660" rx="16" ry="30"/>
    <ellipse class="foliage--deep" cx="355" cy="660" rx="18" ry="28"/>
    <ellipse class="foliage" cx="478" cy="678" rx="34" ry="22"/>
    <ellipse class="foliage" cx="636" cy="655" rx="16" ry="32"/>
    <ellipse class="foliage" cx="738" cy="660" rx="16" ry="30"/>
  </g>

  <!-- base -->
  <rect class="plinth" x="158" y="694" width="681" height="51" fill="var(--plinth)"/>
  <rect x="158" y="745" width="681" height="5" fill="var(--accent-orange)"/>
  <text class="base-label" x="498" y="730" text-anchor="middle">85 THINGS</text>
</svg>
</body>
</html>
```